依頼詳細
袋のデザインと箱のデザインを希望します。
主に40代~60代の主婦層をターゲットに考えています。進物に使えるシンプルだけど高級感のあるイメージ。
因みに、『澄楓』の名前は毛筆で書かれた物で決定しています。
記載項目

サイズ:幅12.5mm×長さ16mm雲竜柄の白い袋を考えています。
栗入り、黒豆入り、あんず入り、ノーマルの4種類で統一感のあるもの。

紙箱(5個・10個・15個入りで同一デザイン)
サイズ:幅220mm×長さ310mm×高さ65mm(10個入り)
紙質:特に無し

希望イメージ
シンプル 複雑
単色 カラフル
暗い 明るい
日常 高級
遊び心 厳粛
未来的 伝統的
女性的 男性的
希望する色
白・黒・オレンジ・紫など
納品ファイル
• 高解像度JPG (.jpg)
• イラストレーター形式 (.ai)
補足説明
同じ大きさで、数種類のどら焼きがあるので、詰合せた時の統一感が出る様にお願いします。
今後も、種類を増やす予定。
この度、パッケージデザインご提案頂きありがとう御座います。

幾つか『澄楓』をsumikazeと表記されてるデザインがありましたので訂正をさせて頂きます。
『澄楓』≒sumika(すみか)です。よろしくお願いいたします。

澄楓の『信』は他界した先代社長から一字取りました。その志を継ぎ、本物を追及しながらも敷居を低くし、『少し贅沢なお菓子』を目指しています。『樂』にはお菓子を食べるシチュエーションを思い浮かべ、その場の雰囲気や人の心など、思わず笑顔になってしまうような空間を作りたいと思ってつけた名前です。

皆様、よろしくお願い致します。
沢山のデザインありがとうございます。

デザインの内容についてお願いがありますので追記致します。

弊社の会社のHPを見て頂いたランサー様の中に弊社の梅のロゴやたかむら製菓舗の名前をデザインに組み込まれてる方がおられますが、今回は弊社本体とはブランドイメージを分けて考えたいと思いますので、あくまで『澄楓』のイメージでロゴないし、デザインの制作をお願いいたします。
■ 選んだ理由

澄楓のブランドイメージを理解して頂き、こちらの細かい修正依頼にも、素早く丁寧に対応して頂きました。

今後もお世話になりたいランサー様に出会う事が出き感謝いたします。

■ 提案者全員のお礼・コメント

この度は、多くのデザインを提案して頂きありがとうございました。
皆さんレベルの高いデザインで選定には時間を要し非常に迷いました。

また、次の機会にも利用したいと思います。

有難うございました。

```html
<!DOCTYPE html>
<html lang="ja">
<head>
<meta charset="utf-8">
<title>澄楓 どら焼き詰合せ箱</title>
<link rel="stylesheet" href="https://fonts.googleapis.com/css2?family=Shippori+Mincho:wght@600&family=Noto+Sans+JP:wght@500&display=swap">
<style>
  :root {
    --plum: #7b2152;
    --band: #ffffff;
    --ribbon: #6b2a8c;
    --mark: #a08d79;
    --mark-text: #ffffff;
  }
  html, body {
    margin: 0;
    padding: 0;
    overflow: hidden;
  }
  body {
    width: 857px;
    height: 1200px;
  }
  .box-lid {
    position: relative;
    width: 857px;
    height: 1200px;
    background: var(--plum);
    overflow: hidden;
  }
  .wrap-band {
    position: absolute;
    left: 0;
    top: 271px;
    width: 857px;
    height: 609px;
    background: var(--band);
  }
  .ribbon-line {
    position: absolute;
    left: 748px;
    top: 0;
    width: 7px;
    height: 100%;
    background: var(--ribbon);
  }
  .ribbon-tag {
    position: absolute;
    left: 723px;
    top: 77px;
  }
  .brand-mark {
    position: absolute;
    left: 386px;
    top: 451px;
    width: 85px;
    height: 135px;
    background: var(--mark);
    display: flex;
    align-items: center;
    justify-content: center;
  }
  .brand-name {
    writing-mode: vertical-rl;
    font-family: "Shippori Mincho", serif;
    font-weight: 600;
    font-size: 50px;
    line-height: 1;
    letter-spacing: 6px;
    color: var(--mark-text);
    margin: 0;
  }
  .brand-roman {
    position: absolute;
    left: 386px;
    top: 596px;
    width: 85px;
    text-align: center;
    font-family: "Noto Sans JP", sans-serif;
    font-weight: 500;
    font-size: 17px;
    letter-spacing: 1px;
    color: var(--mark);
    margin: 0;
  }
</style>
</head>
<body>
  <main class="box-lid">
    <section class="wrap-band">
      <div class="ribbon-line"></div>
      <svg class="ribbon-tag" width="58" height="80" viewBox="0 0 58 80" aria-hidden="true">
        <rect x="0" y="0" width="58" height="80" fill="var(--ribbon)"/>
        <rect x="13" y="22" width="36" height="36" fill="var(--band)"/>
      </svg>
      <div class="brand-mark" style="top:180px">
        <h1 class="brand-name">澄楓</h1>
      </div>
      <p class="brand-roman" style="top:323px">sumika</p>
    </section>
  </main>
</body>
</html>
```